Brochure for Healthy Restaurant Concept

Please design a brochure for our meal prep menu . Include all items and all descriptions of the items . Include some photos. Please ensure you let us know what size paper your design will need to be printed on. Please make it a clean modern design, matching our logo and its ok to use other colors as well. We are open to designs. We dont want it to be too plain.

Include all items including the pre-built options, bundles, and custom meals on the brochure. I will include the old brochure to give you an example, don't copy items and prices from that particular brochure as they could be inaccurate for the "Pre-Built items and breakfast items now.

Industry/Entity Type

Restaurant

Requirements
Must have
• Logo, all menu items
Nice to have
• A QR code linking our website www.plumtreegrillhouse.com

```html
<!DOCTYPE html>
<html lang="en">
<head>
<meta charset="utf-8">
<title>Plum Tree Grill House – Meal Prep Brochure</title>
<link href="https://fonts.googleapis.com/css2?family=Archivo+Black&family=Arimo:ital,wght@0,400;0,700;1,400&display=swap" rel="stylesheet">
<style>
  :root{
    --ink:#1c2912;
    --lime:#8ef000;
    --lime-text:#8ad800;
    --white:#ffffff;
    --rule:#1c2912;
    --body:#1a1a1a;
    --fold:#cfcfcf;
  }
  *{box-sizing:border-box;margin:0;padding:0}
  html,body{width:1200px;height:600px;overflow:hidden;background:#fff}
  body{font-family:"Arimo",Arial,sans-serif;color:var(--body)}
  .spread{position:relative;width:1200px;height:600px;overflow:hidden;background:#fff}
  .abs{position:absolute}
  .heavy{font-family:"Archivo Black","Arial Black",sans-serif}

  /* left panel */
  .photo{position:absolute}
  .bundle-box{left:168px;top:40px;width:167px;height:159px;background:var(--ink)}
  .bundle-title{left:200px;top:66px;color:#fff;font-size:18px;line-height:18px;letter-spacing:.5px}
  .bundle-list{left:200px;top:116px;color:var(--lime);font-size:14.5px;line-height:21px;letter-spacing:.3px}
  .pickup-band{left:0;top:199px;width:335px;height:202px;background:var(--lime)}
  .slogan{left:31px;top:216px;font-family:"Arimo",Arial,sans-serif;font-weight:700;color:var(--ink);line-height:42px;font-size:40px;letter-spacing:-1px}
  .slogan .fresh{display:block;color:#fff;font-family:"Archivo Black","Arial Black",sans-serif;font-size:43px;line-height:44px;letter-spacing:0}
  .delivery{left:206px;top:333px;font-size:12px;line-height:14px;color:var(--ink)}
  .delivery b{font-weight:700}

  /* middle panel */
  .fold-shade{left:370px;top:0;width:230px;height:600px;background:linear-gradient(90deg,#ffffff 0%,#f3f3f3 35%,#dedede 80%,var(--fold) 100%)}
  .vline{position:absolute;width:1px;background:var(--rule)}
  .hrule{position:absolute;height:1px;background:var(--rule)}
  .step-tab{position:absolute;left:376px;width:18px;height:56px;background:var(--ink);color:#fff;font-weight:700;font-size:11px;display:flex;align-items:flex-end;justify-content:center;padding-bottom:12px}
  .section-title{position:absolute;font-size:14.5px;letter-spacing:.6px;color:var(--lime-text);white-space:nowrap}
  .section-title b{color:var(--ink);font-weight:700}
  .note{position:absolute;font-style:italic;font-size:7.6px;color:#444;white-space:nowrap}
  .menu-table{position:absolute;font-size:9.4px;line-height:16.1px;color:var(--body)}
  .menu-row{display:flex;white-space:nowrap}
  .menu-row .oz{color:var(--lime-text);font-style:italic}
  .sub{display:block;font-size:5.6px;line-height:6px;font-style:italic;color:#333;margin-top:-3px;margin-bottom:4px}
  .col-head{position:absolute;font-weight:700;font-size:8.6px;color:var(--lime-text);white-space:nowrap}
  .col-head span{display:inline-block}

  .salad-box{left:533px;top:458px;width:186px;height:102px;background:var(--ink);color:#e6e6e6}
  .salad-title{position:absolute;left:11px;top:12px;font-size:10px;color:#e6e6e6}
  .salad-box .col-head{top:13px;color:var(--lime)}
  .salad-item{position:absolute;left:11px;font-size:9.2px;line-height:11px;color:#d9d9d9}
  .salad-price{position:absolute;font-size:9.2px;color:#fff}

  /* right panel */
  .sauce-bar{left:740px;top:0;width:282px;height:57px;background:var(--lime)}
  .sauce-title{left:740px;top:37px;width:282px;text-align:center;font-weight:700;font-size:14px;color:var(--ink);letter-spacing:.5px}
  .sauce-title .lite{color:#fff}
  .sauce-list{position:absolute;font-size:9.2px;line-height:16.2px;white-space:nowrap}
  .sauce-list small{font-size:5.6px;font-style:italic}
  .seasoned{left:740px;top:165px;width:280px;text-align:center;font-style:italic;font-size:8px;color:#333}
  .extra-head{position:absolute;font-size:14px;line-height:16.5px;color:var(--lime-text);letter-spacing:.4px;white-space:nowrap}
  .extra-head b{display:block;color:var(--ink);font-weight:700}
  .feature-photo{position:absolute;left:740px;width:152px;height:97px}
  .feature-title{position:absolute;left:902px;font-size:18px;line-height:19px;color:var(--ink);letter-spacing:.3px}
  .feature-sub{position:absolute;left:902px;font-size:14px;color:var(--lime-text);letter-spacing:.3px}
  .feature-copy{position:absolute;left:903px;width:119px;font-size:7.8px;line-height:11.2px;text-align:justify;color:#333}

  .brand-strip{left:1043px;top:0;width:157px;height:600px}
  .brand-name{position:absolute;left:1118px;top:300px;transform:translate(-50%,-50%) rotate(-90deg);white-space:nowrap;color:#fff;font-size:27px;letter-spacing:1px}
</style>
</head>
<body>
<main class="spread">

  <!-- LEFT PANEL -->
  <div class="photo" role="img" aria-label="Roasted sweet potato wedges in a meal prep container" style="left:0;top:40px;width:168px;height:159px;background:linear-gradient(135deg,#6b3a1c 0%,#b6541f 35%,#d9772e 60%,#8a5b3a 85%,#a68a6e 100%)"></div>
  <div class="abs bundle-box"></div>
  <h2 class="abs heavy bundle-title">BUNDLES<br>MEAL</h2>
  <div class="abs bundle-list">CARBS<br>PROTEIN<br>VEGGIES</div>

  <div class="abs pickup-band"></div>
  <h1 class="abs slogan">PICK UP<span class="fresh">FRESH</span>EVERY<br>TIME!</h1>
  <p class="abs delivery">Delivery available!<br><b>1 day notice<br>needed</b></p>

  <div class="photo" role="img" aria-label="Broccoli, cauliflower and bell peppers in a meal prep container" style="left:0;top:401px;width:335px;height:159px;background:linear-gradient(160deg,#9b8b78 0%,#e8e4dc 22%,#c9392a 40%,#e6a52a 50%,#5b8a2a 65%,#3c6b1e 85%,#2a3a22 100%)"></div>

  <!-- MIDDLE PANEL -->
  <div class="abs fold-shade"></div>
  <div class="vline" style="left:358px;top:40px;height:135px"></div>
  <div class="vline" style="left:358px;top:425px;height:135px"></div>
  <div class="vline" style="left:719px;top:40px;height:400px"></div>

  <div class="step-tab" style="top:0">1</div>
  <h3 class="section-title" style="left:445px;top:37px">PICK YOUR <b>PROTEIN</b></h3>
  <p class="note" style="left:449px;top:55px">If needing specific weights, please call</p>

  <div class="menu-table" style="left:376px;top:80px">
    <div class="menu-row"><span style="width:71px">StriploinSteak</span><span class="oz" style="width:24px">8oz</span><span>$0.00</span></div>
    <div class="menu-row"><span style="width:71px">ChickenBreast</span><span class="oz" style="width:24px">6oz</span><span>$0.00</span></div>
    <div class="menu-row"><span style="width:71px">Salmon Fillet</span><span class="oz" style="width:24px">6oz</span><span>$0.00</span></div>
    <div class="menu-row"><span style="width:71px">Ground Turkey</span><span class="oz" style="width:24px">4oz</span><span>$0.00</span></div>
    <div class="menu-row"><span style="width:71px">Ground Bison</span><span class="oz" style="width:24px">5oz</span><span>$0.00</span></div>
    <div class="menu-row"><span style="width:71px">Tofu</span><span class="oz" style="width:24px">4oz</span><span>$0.00</span></div>
  </div>
  <div class="menu-table" style="left:564px;top:80px">
    <div class="menu-row"><span style="width:87px">Shrimp</span><span class="oz" style="width:24px">5oz</span><span>$0.00</span></div>
    <div class="menu-row"><span style="width:87px">Lean Beef</span><span class="oz" style="width:24px">5oz</span><span>$0.00</span></div>
    <div class="menu-row"><span style="width:87px">Steak Bites</span><span class="oz" style="width:24px">4oz</span><span>$0.00</span></div>
    <div class="menu-row"><span style="width:87px">Turkey Bites</span><span class="oz" style="width:24px">5oz</span><span>$0.00</span></div>
    <div class="menu-row"><span style="width:87px">Cod Fish</span><span class="oz" style="width:24px">5oz</span><span>$0.00</span></div>
    <div class="menu-row"><span style="width:111px">Verdant Plant Patty</span><span>$0.00</span></div>
  </div>

  <div class="hrule" style="left:450px;top:201px;width:135px"></div>
  <div class="step-tab" style="top:187px">2</div>
  <h3 class="section-title" style="left:445px;top:211px">PICK YOUR <b>VEGGIES</b></h3>
  <div class="col-head" style="left:482px;top:239px"><span style="width:32px">100G</span><span>200G</span></div>
  <div class="col-head" style="left:644px;top:239px"><span style="width:32px">100G</span><span>200G</span></div>

  <div class="menu-table" style="left:376px;top:252px">
    <div class="menu-row"><span style="width:106px">Seasonal Veggies</span><span style="width:32px">$0.00</span><span>$0.00</span></div>
    <span class="sub">(Broccoli, Cauliflower, Bell Peppers)</span>
    <div class="menu-row"><span style="width:106px">Mixed Veggies</span><span style="width:32px">$0.00</span><span>$0.00</span></div>
    <div class="menu-row"><span style="width:106px">Carrots &amp; Peas</span><span style="width:32px">$0.00</span><span>$0.00</span></div>
    <div class="menu-row"><span style="width:106px">Broccoli &amp; Cauliflower</span><span style="width:32px">$0.00</span><span>$0.00</span></div>
    <div class="menu-row"><span style="width:106px">Bell Pepper Mix</span><span style="width:32px">$0.00</span><span>$0.00</span></div>
    <div class="menu-row"><span style="width:106px">The Green Mix</span><span style="width:32px">$0.00</span><span>$0.00</span></div>
    <span class="sub">(Broccoli, Green beans, Asparagus)</span>
  </div>
  <div class="menu-table" style="left:556px;top:252px">
    <div class="menu-row"><span style="width:88px">Asparagus</span><span style="width:32px">$0.00</span><span>$0.00</span></div>
    <div class="menu-row"><span style="width:88px">Green Beans</span><span style="width:32px">$0.00</span><span>$0.00</span></div>
    <div class="menu-row"><span style="width:88px">Broccoli</span><span style="width:32px">$0.00</span><span>$0.00</span></div>
    <div class="menu-row"><span style="width:88px">Carrots</span><span style="width:32px">$0.00</span><span>$0.00</span></div>
    <div class="menu-row"><span style="width:88px">Peas</span><span style="width:32px">$0.00</span><span>$0.00</span></div>
    <div class="menu-row"><span style="width:88px">Cauliflower Custom</span><span style="width:32px">$0.00</span><span>$0.00</span></div>
    <div class="menu-row"><span style="width:88px">Veggie Mix</span><span style="width:32px">$0.00</span><span>$0.00</span></div>
  </div>

  <div class="hrule" style="left:450px;top:395px;width:135px"></div>
  <div class="step-tab" style="top:381px">3</div>
  <h3 class="section-title" style="left:451px;top:405px">PICK YOUR <b>CARBS</b></h3>
  <div class="col-head" style="left:459px;top:440px"><span style="width:32px">100G</span><span>200G</span></div>
  <div class="menu-table" style="left:376px;top:456px;line-height:14.5px">
    <div class="menu-row"><span style="width:83px">Sweet Potatoes</span><span style="width:32px">$0.00</span><span>$0.00</span></div>
    <div class="menu-row"><span style="width:83px">Penne Pasta</span><span style="width:32px">$0.00</span><span>$0.00</span></div>
    <span class="sub" style="margin-top:-1px;margin-bottom:3px">(Gluten free available)</span>
    <div class="menu-row" style="line-height:16.3px"><span style="width:83px">Brown Rice</span><span style="width:32px">$0.00</span><span>$0.00</span></div>
    <div class="menu-row" style="line-height:16.3px"><span style="width:83px">Basmati Rice</span><span style="width:32px">$0.00</span><span>$0.00</span></div>
    <div class="menu-row" style="line-height:16.3px"><span style="width:83px">Quinoa</span><span style="width:32px">$0.00</span><span>$0.00</span></div>
    <div class="menu-row" style="line-height:16.3px"><span style="width:83px">Baby Potatoes</span><span style="width:32px">$0.00</span><span>$0.00</span></div>
  </div>

  <section class="abs salad-box">
    <h4 class="salad-title heavy">ADD A SALAD</h4>
    <div class="col-head" style="left:109px"><span style="width:32px">100G</span><span>200G</span></div>
    <p class="salad-item" style="top:31px">Strawberry Spinach<br>Salad</p>
    <span class="salad-price" style="left:109px;top:31px">$0.00</span>
    <span class="salad-price" style="left:141px;top:31px">$0.00</span>
    <p class="salad-item" style="top:62px">Cranberry Pecan<br>Salad</p>
    <span class="salad-price" style="left:109px;top:62px">$0.00</span>
    <span class="salad-price" style="left:141px;top:62px">$0.00</span>
  </section>

  <!-- RIGHT PANEL -->
  <div class="abs sauce-bar"></div>
  <h3 class="abs sauce-title"><span class="lite">ADD</span> SAUCES &nbsp;$0.50</h3>
  <div class="sauce-list" style="left:757px;top:72px">
    Sweet Chili Thai Sauce<br>Teriyaki Sauce Chipotle<br>Mayo Sriracha Hot Sauce<br>Pesto <small>(Pasta Sauce)</small><br>Tomato Basil <small>(Pasta Sauce)</small>
  </div>
  <div class="sauce-list" style="left:894px;top:72px">
    Barbeque Sauce Sweet and<br>Sour Balsamic <small>(Salad Dressing)</small><br>Gluten Free Teriyaki Sauce
  </div>
  <p class="abs seasoned">All protein, veggies and carbs will be seasoned.</p>

  <div class="hrule" style="left:811px;top:201px;width:136px"></div>
  <h3 class="extra-head" style="left:739px;top:211px">HOUSEMADE &nbsp;<span style="font-weight:700">$1.00</span><b>DRESSINGS</b></h3>
  <h3 class="extra-head" style="left:889px;top:211px">ADDITIONAL<b>OPTIONS</b></h3>
  <div class="menu-table" style="left:739px;top:252px">
    <div class="menu-row">Sesame Ginger Vinaigrette</div>
    <div class="menu-row">Lime Ginger Dill</div>
    <div class="menu-row">Horseradish Ranch</div>
  </div>
  <div class="menu-table" style="left:889px;top:252px">
    <div class="menu-row"><span style="width:107px">Half Avocado</span><span>$0.00</span></div>
    <div class="menu-row"><span style="width:79px">Cheese</span><span class="oz" style="width:28px">1oz</span><span>$0.00</span></div>
    <div class="menu-row"><span style="width:79px">Raw Onion</span><span class="oz" style="width:28px">1oz</span><span>$0.00</span></div>
    <div class="menu-row"><span style="width:79px">Raw Mushroom</span><span class="oz" style="width:28px">1oz</span><span>$0.00</span></div>
  </div>
  <div class="hrule" style="left:811px;top:337px;width:136px"></div>

  <div class="feature-photo" role="img" aria-label="Glazed chicken with rice and vegetables in a meal prep container" style="top:351px;background:linear-gradient(135deg,#7a8a96 0%,#1d2a3a 30%,#6a4022 50%,#c68a3a 62%,#3f6b24 78%,#9aa2a8 100%)"></div>
  <h3 class="feature-title heavy" style="top:352px">PREP-BUILT</h3>
  <p class="feature-sub" style="top:369px">MEALS</p>
  <p class="feature-copy" style="top:394px">Lorem ipsum dolor sit amet consectetuer odio non tellus natoque accumsan. Sed hac enim Lorem tempus tortor justo eget scelerisque.</p>

  <div class="feature-photo" role="img" aria-label="Grilled steak garnished with herbs" style="top:463px;border:1px solid #555;background:radial-gradient(ellipse at 50% 60%,#8a3a2a 0%,#5a2418 40%,#ffffff 72%)"></div>
  <h3 class="feature-title heavy" style="top:463px">CUSTOM</h3>
  <p class="feature-sub" style="top:480px">MEALS</p>
  <p class="feature-copy" style="top:506px">Lorem ipsum dolor sit amet consectetuer odio non tellus natoque accumsan. Sed hac enim Lorem tempus tortor justo eget scelerisque.</p>

  <div class="abs brand-strip" role="img" aria-label="Close-up of fresh cauliflower heads and green leaves" style="background:linear-gradient(180deg,#3e4a38 0%,#d9d9d2 18%,#7d8c70 40%,#e8e8e2 55%,#4f5d45 72%,#cfcfc8 88%,#6b7762 100%)"></div>
  <p class="brand-name heavy">PLUM TREE GRILL HOUSE</p>

</main>
</body>
</html>
```